Thornwell Building Company - advertisement poster

I am looking to print some canvas signs to advertise my general contracting company, Thornwell Building Company. The sign will measure 6' long x 3' high so the size should match that ratio. I already have a logo icon, which is the Letter 'A' and some trees that I would like to incorporate, see attached. I would also like the to have the following information listed:
1) phone number: 472-318-6095
2) email: thornwellbuildingcompany@mailvistra.net
3) website: thornwellbuildingcompany.com
4) Lic#5386204
5) I want to use this text: "BUILD WITH THE T-CREW!"

The ad should be relatively simple and clean. Black and Green are my company colors. I am open to creative ideas!

Target Market(s)

People looking to renovate their homes

Industry/Entity Type

Construction

Colors
59FF00
82FF00
B8FF75
E3FFCB
F4FFEA

Requirements
Must have
• Must have my company logo
Should not have
• No photos or complex graphics

```html
<!DOCTYPE html>
<html lang="en">
<head>
<meta charset="utf-8">
<title>Thornwell Building Company – Banner</title>
<link rel="stylesheet" href="https://fonts.googleapis.com/css2?family=Montserrat:wght@700;800&family=Open+Sans:wght@400;700&display=swap">
<style>
  :root {
    --page-bg: #dcdcdc;
    --banner-bg: #ffffff;
    --ink: #231f20;
    --night: #2b2b2b;
    --forest: #8ed26a;
    --forest-light: #a6e084;
    --scene-light: #eeeeee;
    --scene-dark: #d2d2d2;
    --text-light: #ffffff;
  }
  html, body {
    margin: 0;
    width: 1200px;
    height: 1000px;
    overflow: hidden;
    background: var(--page-bg);
  }
  .banner {
    position: absolute;
    left: 40px;
    top: 220px;
    width: 1120px;
    height: 560px;
    background: var(--banner-bg);
    overflow: hidden;
  }
  .banner-art {
    position: absolute;
    inset: 0;
  }
  .headline {
    position: absolute;
    left: 0;
    width: 100%;
    text-align: center;
    margin: 0;
    font-family: "Montserrat", Arial, sans-serif;
    font-weight: 800;
    line-height: 1;
  }
  .headline-top {
    top: 110px;
    font-size: 56px;
    color: var(--ink);
  }
  .headline-crew {
    top: 325px;
    font-size: 46px;
    color: var(--text-light);
  }
  .contact {
    position: absolute;
    left: 0;
    top: 394px;
    width: 100%;
    text-align: center;
    color: var(--text-light);
    font-family: "Open Sans", Arial, sans-serif;
  }
  .contact-phone {
    margin: 0 0 2px;
    font-weight: 700;
    font-size: 36px;
    line-height: 1.1;
  }
  .contact-line {
    margin: 0;
    font-size: 18px;
    line-height: 25px;
  }
  .brand {
    position: absolute;
    right: 62px;
    top: 30px;
    width: 140px;
    text-align: center;
    font-family: "Montserrat", Arial, sans-serif;
    font-weight: 700;
    color: var(--ink);
  }
  .brand-mark {
    display: block;
    width: 22px;
    height: 22px;
    margin: 0 auto 6px;
    background: var(--forest);
  }
  .brand-name {
    display: block;
    font-size: 17px;
    letter-spacing: 0.5px;
    line-height: 1.1;
  }
  .brand-sub {
    display: block;
    font-size: 8px;
    letter-spacing: 2.4px;
    line-height: 1.3;
  }
</style>
</head>
<body>
  <main class="banner">
    <svg class="banner-art" width="1120" height="560" viewBox="0 0 1120 560" xmlns="http://www.w3.org/2000/svg">
      <defs>
        <linearGradient id="scene-fade" x1="0" y1="0" x2="0" y2="1">
          <stop offset="0" stop-color="var(--scene-light)"/>
          <stop offset="1" stop-color="var(--scene-dark)"/>
        </linearGradient>
      </defs>
      <rect class="construction-scene" x="60" y="28" width="1025" height="345" fill="url(#scene-fade)" role="img" aria-label="Tower cranes and building frames under construction, in black silhouette"/>
      <polygon class="tree-line" role="img" aria-label="Row of green pine trees rising toward the centre"
        fill="var(--forest)"
        points="0,488 0,395 70,355 160,320 255,270 355,220 465,178 560,168 655,178 765,220 865,270 960,320 1050,355 1120,380 1120,488"/>
      <polygon class="hill" fill="var(--night)"
        points="0,488 42,488 42,459 114,459 114,429 187,429 187,399 256,399 256,370 325,370 325,340 398,340 398,310 467,310 467,281 653,281 653,310 708,310 708,340 781,340 781,370 850,370 850,399 919,399 919,429 992,429 992,459 1065,459 1065,488 1120,488 1120,560 0,560"/>
    </svg>

    <h1 class="headline headline-top">BUILD WITH THE</h1>
    <p class="headline headline-crew">T-CREW!</p>

    <div class="contact">
      <p class="contact-phone">472-318-6095</p>
      <p class="contact-line">email: thornwellbuildingcompany@mailvistra.net</p>
      <p class="contact-line">thornwellbuildingcompany.com</p>
      <p class="contact-line">Lic#5386204</p>
    </div>

    <div class="brand">
      <span class="brand-mark"></span>
      <span class="brand-name">THORNWELL</span>
      <span class="brand-sub">BUILDING COMPANY</span>
    </div>
  </main>
</body>
</html>
```